Wordpress Web Design & Coding for velqorahealth.ca

We need a website for a new investment company that is visually grabbing and vibrant. We would like to see a web page that displays trust, growth and confidence. Needs to be responsive and mobile friendly for all browsers and coded for both Android & IOS.

Open to the number of pages and menu items. I selected 4 but if you feel the layout would work better with less I am open to this. Need to sell the people (management team/related businesses) and then show where the invested money will be going (upcoming projects).

Company Info:

Velq Ora is an investment company put together by a group of seasoned business professionals who have come together to combine decades of success in the real estate development, management, financing and medical services. The company will be a full service company offering turn key solutions for medical professionals.

Velq-Ora will focus on providing a full range of services via a group of distinct companies to deliver newly emerging needs of the medical community. The end goal will be to create complete solutions for individuals in the medical community. Our group has experience and success with the conceptualization, construction and financing of medical and dental clinic spaces. Velq-Ora Solutions will be established to accommodate all areas of the development and creation of clinics for medical professionals from building construction to equipment financing and administrations.

You can mention these companies and take photos from their websites. You can also use stock photos.

Our construction partner:
https://812bld.com/projects/

Our equipment leasing partner:
https://www.lomerix.com/

Our Management Team and medical partners

Dale Pickett
https://www.yourcalmpath.ca/

Milos Vandergrift
https://www.qhzdentalservices.com/about-us

PROPOSED PROJECTS (see attachment for details)
Harlow Ridge Business Park
Dunmere Business Park
Mt. Corwin Way Professional

Target Market(s)

Investors

Industry/Entity Type

Investment

Coding

Coded - Design and coding required

Number of Pages Required

4 page

Font styles to use
Sans Serif

Requirements
Must have
• Wordpress – must be both desktop and mobile friendly with fast page load speed
Ability to edit after ourselves in Wordpress
Attractive home page with logo etc.
Logo colours are: for the blue the pantone color is #0355a3
and for the green is #8cc63f

Sections, about us, what we do/services we provide, contact us

```html
<!DOCTYPE html>
<html lang="en">
<head>
<meta charset="utf-8">
<title>Velq-Ora Solutions</title>
<link rel="stylesheet" href="https://fonts.googleapis.com/css2?family=Roboto:wght@400;500;700&display=swap">
<style>
:root{
  --blue:#0355a3;
  --blue-deep:#0d4f9c;
  --green:#8cc63f;
  --ink:#222;
  --text:#333;
  --muted:#444;
  --band:#f4f4f4;
  --line:#d6d6d6;
  --white:#fff;
}
*{margin:0;padding:0;box-sizing:border-box}
html,body{width:1200px;height:2741px;overflow:hidden}
body{position:relative;background:var(--white);font-family:"Roboto",Arial,sans-serif;color:var(--text)}
a{color:inherit;text-decoration:none}

/* header */
.site-header{position:absolute;left:0;top:0;width:1200px;height:109px;background:var(--white)}
.brand{position:absolute;left:112px;top:34px;display:flex;align-items:center;gap:8px}
.brand-mark{width:14px;height:14px;background:var(--green)}
.brand-name{font-weight:700;font-size:26px;color:var(--blue);letter-spacing:.5px}
.main-nav a{position:absolute;top:51px;font-size:16px;color:var(--ink)}
.main-nav a.current{color:var(--blue)}
.call-icon{position:absolute;left:891px;top:47px;width:34px;height:34px;border-radius:50%;background:#1aa345;display:flex;align-items:center;justify-content:center}
.call-text{position:absolute;left:941px;top:33px;font-weight:700;font-size:19px;color:var(--ink);line-height:27px}

/* hero */
.hero{position:absolute;left:0;top:109px;width:1200px;height:573px;background:linear-gradient(135deg,#3b4452 0%,#8f8f8e 35%,#c9c5bd 55%,#7c8aa0 80%,#3e4c64 100%)}
.hero-title{position:absolute;left:0;width:1200px;top:272px;text-align:center;font-weight:700;font-size:70px;color:var(--white);text-shadow:0 2px 6px rgba(0,0,0,.5)}
.hero-sub{position:absolute;left:0;width:1200px;top:370px;text-align:center;font-weight:500;font-size:20px;line-height:31px;color:var(--white);text-shadow:0 1px 4px rgba(0,0,0,.6)}
.btn-primary{position:absolute;left:523px;top:454px;width:154px;height:50px;background:var(--blue);color:var(--white);font-weight:700;font-size:17px;display:flex;align-items:center;justify-content:center;border-radius:3px}
.slider-dots{position:absolute;left:570px;top:630px;display:flex;gap:12px;align-items:center}
.slider-dots span{width:9px;height:9px;border-radius:50%;background:var(--white)}
.slider-dots span.on{width:12px;height:12px}
.hero-rail{position:absolute;left:1088px;width:1px;background:rgba(255,255,255,.8)}
.social-dot{position:absolute;width:36px;height:36px;border-radius:50%;background:var(--blue);border:2px solid var(--white);display:flex;align-items:center;justify-content:center}
.social-dot::after,.f-social::after{content:"";width:8px;height:8px;border-radius:50%;background:var(--white)}

/* section titles */
.sec-title{position:absolute;font-weight:700;font-size:40px;color:var(--blue);letter-spacing:.5px}
.rule{position:absolute;height:4px;background:var(--green);border-radius:2px}

/* about */
.about-back{position:absolute;left:111px;top:782px;width:374px;height:298px;background:linear-gradient(120deg,#4a5a2c,#a0793f 45%,#d9b48a 70%,#8a6a45);border:2px solid #b9d4f0}
.about-frame{position:absolute;left:226px;top:883px;width:290px;height:260px;background:var(--white)}
.about-front{position:absolute;left:241px;top:898px;width:260px;height:244px;background:linear-gradient(135deg,#1d1f24,#3a3d44 50%,#9a4a4a 75%,#e2e2e2)}
.about-copy{position:absolute;left:551px;top:852px;width:545px;font-size:15px;line-height:34.3px;color:var(--text)}
.btn-green{position:absolute;left:556px;top:1081px;width:136px;height:45px;background:var(--green);color:var(--white);font-weight:700;font-size:17px;display:flex;align-items:center;justify-content:center;border-radius:2px}

/* services */
.services{position:absolute;left:0;top:1254px;width:1200px;height:647px;background:var(--band)}
.center-copy{position:absolute;left:0;width:1200px;text-align:center;font-size:15px;line-height:31px;color:var(--text)}
.service-card{position:absolute;top:1510px;width:301px;height:322px;background:var(--white);border:1px solid var(--line);box-shadow:0 1px 3px rgba(0,0,0,.12)}
.service-photo{position:absolute;left:0;top:0;width:100%;height:179px;clip-path:polygon(0 0,100% 0,100% 100%,50% 80%,0 100%)}
.service-icon{position:absolute;left:120px;top:128px;width:60px;height:60px;border-radius:50%;background:var(--blue);border:3px solid var(--white);display:flex;align-items:center;justify-content:center}
.service-name{position:absolute;top:202px;width:100%;text-align:center;font-weight:500;font-size:18px;color:var(--ink)}
.service-desc{position:absolute;top:238px;width:100%;text-align:center;font-size:13.5px;line-height:22.5px;color:var(--muted)}
.carousel-arrow{position:absolute;top:1666px;width:38px;height:38px;border-radius:50%;border:1px solid #9a9a9a;background:var(--white);display:flex;align-items:center;justify-content:center}

/* partners */
.partner{position:absolute;top:2131px;height:114px;border:1px solid var(--line);display:flex;align-items:center;justify-content:center;background:var(--white)}
.partner-name{font-size:22px;font-weight:500;color:var(--ink)}

/* footer */
.site-footer{position:absolute;left:0;top:2350px;width:1200px;height:391px;background:var(--blue-deep);color:var(--white)}
.f-head{position:absolute;top:90px;font-weight:500;font-size:22px;letter-spacing:1px;color:var(--white)}
.f-link{position:absolute;font-size:17px;display:flex;align-items:center;gap:12px;color:var(--white)}
.f-contact{position:absolute;left:342px;font-size:17px;line-height:32px;display:flex;gap:18px;color:var(--white)}
.f-contact svg{flex:none;margin-top:7px}
.f-brand{position:absolute;left:937px;top:112px;width:148px;text-align:center;font-weight:700;font-size:26px;color:var(--white)}
.f-social{position:absolute;top:2529px;width:37px;height:37px;border-radius:50%;border:1.5px solid var(--white);display:flex;align-items:center;justify-content:center}
.copyright{position:absolute;left:0;width:1200px;top:2700px;text-align:center;font-size:14px;color:var(--white)}
</style>
</head>
<body>

<header class="site-header">
  <div class="brand"><span class="brand-mark"></span><span class="brand-name">VELQ-ORA</span></div>
  <nav class="main-nav">
    <a class="current" href="#" style="left:318px">HOME</a>
    <a href="#" style="left:394px">ABOUT</a>
    <a href="#" style="left:476px">SERVICES</a>
    <a href="#" style="left:584px">PARTNERS</a>
    <a href="#" style="left:697px">PROJECTS</a>
    <a href="#" style="left:809px">TEAM</a>
  </nav>
  <div class="call-icon"><svg width="18" height="18" viewBox="0 0 24 24"><path fill="#fff" d="M6.6 10.8a15.1 15.1 0 0 0 6.6 6.6l2.2-2.2c.3-.3.7-.4 1-.2 1.1.4 2.3.6 3.6.6.6 0 1 .4 1 1V20c0 .6-.4 1-1 1A17 17 0 0 1 3 4c0-.6.4-1 1-1h3.5c.6 0 1 .4 1 1 0 1.3.2 2.5.6 3.6.1.3 0 .7-.2 1z"/></svg></div>
  <div class="call-text">Call Us<br>(800) 555-0142</div>
</header>

<section class="hero" role="img" aria-label="Photo of business people reviewing financial charts at a desk with laptop and calculators"></section>
<h1 class="hero-title">Velq-Ora Solutions</h1>
<p class="hero-sub">Neque porro quisquam est qui dolorem ipsum quia dolor sit amet,<br>consectetur, adipisci velit.</p>
<a class="btn-primary" href="#">GET STARTED</a>
<div class="slider-dots"><span></span><span class="on"></span><span></span></div>
<div class="hero-rail" style="top:236px;height:112px"></div>
<div class="hero-rail" style="top:532px;height:112px"></div>
<span class="social-dot" style="left:1070px;top:370px" aria-label="Social link"></span>
<span class="social-dot" style="left:1070px;top:422px" aria-label="Social link"></span>
<span class="social-dot" style="left:1070px;top:474px" aria-label="Social link"></span>

<div class="about-back" role="img" aria-label="Photo of coin stacks with a rising arrow"></div>
<div class="about-frame"></div>
<div class="about-front" role="img" aria-label="Photo of a hand placing a rising arrow over small model houses"></div>
<h2 class="sec-title" style="left:551px;top:766px">ABOUT US</h2>
<span class="rule" style="left:551px;top:820px;width:75px"></span>
<span class="rule" style="left:636px;top:820px;width:24px"></span>
<p class="about-copy">Lorem ipsum dolor sit amet, consectetur adipiscing elit, sed do eiusmod tempor incididunt ut labore et dolore magna aliqua. Ut enim ad minim veniam, quis nostrud exercitation ullamco laboris nisi ut aliquip ex ea commodo consequat. Duis aute irure dolor in reprehenderit in voluptate velit esse cillum dolore eu fugiat nulla pariatur. Excepteur sint occaecat cupidatat non proident, sunt in culpa qui officia deserunt mollit anim id est laborum</p>
<a class="btn-green" href="#">READ MORE</a>

<section class="services"></section>
<h2 class="sec-title" style="left:0;width:1200px;text-align:center;top:1315px">OUR SERVICES</h2>
<span class="rule" style="left:547px;top:1379px;width:73px"></span>
<span class="rule" style="left:632px;top:1379px;width:21px"></span>
<p class="center-copy" style="top:1406px">Lorem ipsum dolor sit amet, consectetur adipiscing elit, sed do eiusmod tempor incididunt<br>ut labore et dolore magna aliqua.</p>

<div class="carousel-arrow" style="left:48px"><svg width="18" height="12" viewBox="0 0 18 12"><path d="M17 6H2M6 1 1 6l5 5" fill="none" stroke="#555" stroke-width="1.4"/></svg></div>
<div class="carousel-arrow" style="left:1111px"><svg width="18" height="12" viewBox="0 0 18 12"><path d="M1 6h15M12 1l5 5-5 5" fill="none" stroke="#555" stroke-width="1.4"/></svg></div>

<article class="service-card" style="left:111px">
  <div class="service-photo" role="img" aria-label="Photo of a hand holding a small model house and keys" style="background:linear-gradient(135deg,#eae7e2,#c9c2ba 50%,#f3f3f3)"></div>
  <div class="service-icon"><svg width="28" height="28" viewBox="0 0 24 24" fill="none" stroke="#fff" stroke-width="1.4"><rect x="8" y="3" width="10" height="13"/><path d="M10 6h2M14 6h2M10 9h2M14 9h2M10 12h2M14 12h2M2 18c3 0 5-2 8-2h5c1 0 1 2 0 2h-4M2 21h13l6-4"/></svg></div>
  <h3 class="service-name">Real Estate development</h3>
  <p class="service-desc">At vero eos et accusamus et iusto odio<br>dignissimos ducimus qui blanditiis<br>praesentium voluptatum deleniti atque</p>
</article>

<article class="service-card" style="left:450px">
  <div class="service-photo" role="img" aria-label="Aerial photo of construction workers on a rebar site" style="background:linear-gradient(135deg,#7d7a74,#5a5650 45%,#c9a23a 70%,#6a665e)"></div>
  <div class="service-icon"><svg width="28" height="28" viewBox="0 0 24 24" fill="none" stroke="#fff" stroke-width="1.6"><path d="M4 20 14 10M15 4a4 4 0 0 0 5 5l-3 3-5-5zM4 4l4 4M20 20l-7-7"/></svg></div>
  <h3 class="service-name">Construction</h3>
  <p class="service-desc">At vero eos et accusamus et iusto odio<br>dignissimos ducimus qui blanditiis<br>praesentium voluptatum deleniti atque</p>
</article>

<article class="service-card" style="left:784px">
  <div class="service-photo" role="img" aria-label="Photo of a medical professional with a tablet beside a glowing DNA graphic" style="background:linear-gradient(135deg,#0b3a52,#1b7a99 45%,#6fc3d8 70%,#d9e8f0)"></div>
  <div class="service-icon"><svg width="28" height="28" viewBox="0 0 24 24" fill="none" stroke="#fff" stroke-width="1.5"><path d="M12 16s-5-3-5-6a2.5 2.5 0 0 1 5-1 2.5 2.5 0 0 1 5 1c0 3-5 6-5 6zM3 14l4 4h9M21 10l-4-4H8"/></svg></div>
  <h3 class="service-name">Medical solution,</h3>
  <p class="service-desc">At vero eos et accusamus et iusto odio<br>dignissimos ducimus qui blanditiis<br>praesentium voluptatum deleniti atque</p>
</article>

<h2 class="sec-title" style="left:0;width:1200px;text-align:center;top:1985px">OUR PARTNER</h2>
<span class="rule" style="left:547px;top:2048px;width:73px"></span>
<span class="rule" style="left:632px;top:2048px;width:21px"></span>
<div class="partner" style="left:104px;width:228px"><span class="partner-name">812 Builders Inc.</span></div>
<div class="partner" style="left:361px;width:226px"><span class="partner-name">Lomerix Leasing</span></div>
<div class="partner" style="left:611px;width:226px"><span class="partner-name">QHZ Dental</span></div>
<div class="partner" style="left:858px;width:227px"><span class="partner-name">calmpath</span></div>

<footer class="site-footer">
  <h4 class="f-head" style="left:109px">QUICK LINKS</h4>
  <h4 class="f-head" style="left:342px">CONTACT US</h4>
  <h4 class="f-head" style="left:695px">INFO</h4>
  <div class="f-brand">VELQ-ORA</div>
</footer>

<a class="f-link" href="#" style="left:112px;top:2481px"><svg width="9" height="14" viewBox="0 0 9 14"><path d="M1 1l6 6-6 6" fill="none" stroke="#fff" stroke-width="1.6"/></svg>Home</a>
<a class="f-link" href="#" style="left:112px;top:2519px"><svg width="9" height="14" viewBox="0 0 9 14"><path d="M1 1l6 6-6 6" fill="none" stroke="#fff" stroke-width="1.6"/></svg>About Us</a>
<a class="f-link" href="#" style="left:112px;top:2557px"><svg width="9" height="14" viewBox="0 0 9 14"><path d="M1 1l6 6-6 6" fill="none" stroke="#fff" stroke-width="1.6"/></svg>Services</a>
<a class="f-link" href="#" style="left:112px;top:2595px"><svg width="9" height="14" viewBox="0 0 9 14"><path d="M1 1l6 6-6 6" fill="none" stroke="#fff" stroke-width="1.6"/></svg>Contact Us</a>

<div class="f-contact" style="top:2468px"><svg width="16" height="20" viewBox="0 0 16 20"><path fill="#fff" d="M8 0a7 7 0 0 0-7 7c0 5 7 13 7 13s7-8 7-13a7 7 0 0 0-7-7zm0 10a3 3 0 1 1 0-6 3 3 0 0 1 0 6z"/></svg><span>Sed ut perspiciatis unde omnis<br>iste natus error sit voluptatem</span></div>
<div class="f-contact" style="top:2545px"><svg width="18" height="18" viewBox="0 0 24 24"><path fill="#fff" d="M6.6 10.8a15.1 15.1 0 0 0 6.6 6.6l2.2-2.2c.3-.3.7-.4 1-.2 1.1.4 2.3.6 3.6.6.6 0 1 .4 1 1V20c0 .6-.4 1-1 1A17 17 0 0 1 3 4c0-.6.4-1 1-1h3.5c.6 0 1 .4 1 1 0 1.3.2 2.5.6 3.6.1.3 0 .7-.2 1z"/></svg><span>888-555-0199</span></div>
<div class="f-contact" style="top:2598px"><svg width="24" height="18" viewBox="0 0 24 18"><rect x="1" y="1" width="22" height="16" fill="none" stroke="#fff" stroke-width="1.4"/><path d="M1 1l11 9 11-9M1 17l8-8M23 17l-8-8" fill="none" stroke="#fff" stroke-width="1.4"/></svg><span>info@velqorahealth.ca</span></div>

<a class="f-link" href="#" style="left:698px;top:2476px;gap:18px"><svg width="9" height="14" viewBox="0 0 9 14"><path d="M1 1l6 6-6 6" fill="none" stroke="#fff" stroke-width="1.6"/></svg>Terms and conditions</a>
<a class="f-link" href="#" style="left:698px;top:2514px;gap:18px"><svg width="9" height="14" viewBox="0 0 9 14"><path d="M1 1l6 6-6 6" fill="none" stroke="#fff" stroke-width="1.6"/></svg>Site Map</a>
<a class="f-link" href="#" style="left:698px;top:2552px;gap:18px"><svg width="9" height="14" viewBox="0 0 9 14"><path d="M1 1l6 6-6 6" fill="none" stroke="#fff" stroke-width="1.6"/></svg>Privacy policy</a>

<span class="f-social" style="left:937px" aria-label="Social link"></span>
<span class="f-social" style="left:990px" aria-label="Social link"></span>
<span class="f-social" style="left:1048px" aria-label="Social link"></span>

<p class="copyright">Copyrights © 2020 Copyrights Company Name | All Rights Reserved</p>

</body>
</html>
```